Info Graphic about Maple Orchard Restaurant

This info graphic should detail all releavent details about Maple Orchard, such as opening hours, accepted payment methods, home delivery areas etc. please refer attached word document for details.

Also attached a pdf with old info graphic.

IMPORTANT:. Given there is lot of text, I expect the designer to make this interesting. This will be printed in A1 and also A4
Also, I need this in both Portrait and landscape designs.

Industry/Entity Type

Hospitality

Font styles to use
Serif
Sans Serif
Decorative
Script
Other font styles liked:
• I let designer choose

Colors

Designer to choose colors to be used in the design.

Requirements
Must have
• Refer attached word doc
Nice to have
• Refer attached word doc
Should not have
• Refer attached word doc

```html
<!DOCTYPE html>
<html lang="en">
<head>
<meta charset="utf-8">
<title>Maple Orchard Indian Restaurant – Info Sheet</title>
<link rel="stylesheet" href="https://fonts.googleapis.com/css2?family=Montserrat:wght@400;500;600;700;800&display=swap">
<style>
:root{
  --bg:#a7a9ac;
  --paper:#ffffff;
  --red:#b52a2e;
  --deep-red:#9e1f24;
  --orange:#f08c1e;
  --yellow:#f5c12e;
  --lime:#c7c43a;
  --ink:#2b2b2b;
  --grey:#555;
}
*{box-sizing:border-box;margin:0;padding:0}
html,body{width:1200px;height:1000px;overflow:hidden;background:var(--bg)}
body{font-family:"Montserrat",Arial,sans-serif;color:var(--ink);position:relative}
.sheet{position:absolute;left:302px;top:78px;width:596px;height:844px;background:var(--paper)}
.abs{position:absolute}
.chillies{position:absolute;border-radius:40% 40% 50% 50%;background:linear-gradient(90deg,var(--deep-red),var(--red) 40%,var(--orange) 70%,var(--lime))}
.brand{left:110px;width:376px;top:54px;text-align:center;font-family:"Montserrat",Arial,sans-serif;font-weight:800;font-size:40px;line-height:48px;color:var(--red)}
.tagline{left:110px;width:376px;top:112px;text-align:center;font-weight:700;font-size:16px;letter-spacing:3px;color:var(--ink)}
.site{left:0;width:596px;top:160px;text-align:center;font-size:12px;letter-spacing:4.5px;color:var(--ink)}
.band{left:10px;width:580px;height:12px;background:linear-gradient(90deg,var(--red),var(--orange) 55%,var(--yellow) 75%,var(--lime));clip-path:polygon(0 35%,100% 0,100% 100%,0 100%)}
.rule{background:var(--ink);height:3px}
.vrule{left:299px;top:205px;width:3px;height:530px;background:var(--ink)}
.hours-sign{left:18px;top:236px;width:108px;height:60px;background:var(--orange);transform:rotate(-14deg);padding:5px}
.hours-sign span{display:flex;width:100%;height:100%;background:var(--deep-red);color:#fff;font-weight:800;font-size:14px;line-height:16px;text-align:center;align-items:center;justify-content:center}
.day{color:var(--red);font-weight:800;font-size:14px;letter-spacing:-.3px}
.tiny{font-size:8px;color:var(--grey);line-height:9px}
.time{font-weight:800;font-size:13px;line-height:14px}
.hours{left:137px;top:224px}
.dash{border-top:1.5px dashed var(--ink)}
.note{background:var(--yellow);font-size:8px;text-align:center;line-height:11px;padding:3px 0}
.head{color:var(--red);font-weight:800}
.suburbs{font-weight:700;font-size:12px;line-height:16px}
.charges{left:30px;top:568px;width:256px;height:32px;background:var(--yellow);display:flex;font-size:8px;text-align:center}
.charges div{flex:1;padding-top:3px}
.charges b{display:block;font-size:15px;font-weight:500;margin-top:1px}
.charges div+div{border-left:1.5px solid var(--ink)}
.icon-fill{background:var(--ink)}
.voucher{left:318px;top:228px;width:258px;height:108px;border:1.5px dashed var(--ink);border-radius:10px;padding:6px 10px;font-size:9.5px;line-height:13px}
.voucher h3{color:var(--red);font-weight:800;font-size:18px;text-align:center;margin-bottom:4px}
.bullet{position:relative;padding-left:8px}
.bullet:before{content:"";position:absolute;left:0;top:4px;width:5px;height:5px;border-radius:50%;background:var(--ink)}
.pill{left:318px;top:452px;width:258px;height:26px;border:2px solid var(--ink);border-radius:13px;background:linear-gradient(90deg,var(--red),var(--orange) 60%,var(--lime));color:#fff;font-weight:800;font-size:14px;text-align:center;line-height:22px}
.pay{position:absolute;height:28px;border-radius:4px;font-size:10px;font-weight:700;display:flex;align-items:center;justify-content:center;text-align:center;line-height:10px}
.pay.light{border:1px solid #223a7a;color:#223a7a;background:#fff}
.services{font-weight:700;font-size:12px;line-height:16px}
.partner{position:absolute;top:772px}
</style>
</head>
<body>
<main class="sheet">
  <div class="chillies" style="left:30px;top:36px;width:80px;height:134px" role="img" aria-label="Bunch of red, orange and green chillies"></div>
  <div class="chillies" style="left:486px;top:36px;width:80px;height:134px;transform:scaleX(-1)" role="img" aria-label="Bunch of red, orange and green chillies"></div>
  <h1 class="abs brand">Maple Orchard</h1>
  <div class="abs tagline">INDIAN RESTAURANT</div>
  <div class="abs site">WWW.MAPLEORCHARD.COM.AU</div>
  <div class="abs band" style="top:186px"></div>
  <div class="abs rule" style="left:10px;width:580px;top:203px"></div>
  <div class="abs vrule"></div>

  <svg class="abs" style="left:46px;top:206px" width="40" height="34" viewBox="0 0 40 34"><circle cx="20" cy="6" r="4" fill="none" stroke="#555" stroke-width="2"/><path d="M18 9 L4 32 M22 9 L36 28" stroke="#555" stroke-width="1.5" fill="none"/></svg>
  <div class="abs hours-sign"><span>OPENING<br>HOURS</span></div>
  <section class="abs hours">
    <div class="day">MONDAY-FRIDAY</div>
    <div class="tiny">Morning</div><div class="time">11:30 AM - 2:30 PM</div>
    <div class="tiny">Evening</div><div class="time">5:00 PM- 9:00 PM</div>
    <div class="day" style="margin-top:8px">SATURDAY-SUNDAY</div>
    <div class="tiny">Morning</div><div class="time">9:30 AM - 2:30 PM</div>
    <div class="tiny">Evening</div><div class="time">5:00 PM- 9:00 PM</div>
  </section>
  <div class="abs dash" style="left:30px;width:256px;top:364px"></div>
  <div class="abs note" style="left:30px;width:256px;top:370px">* Dinner Buffet is available only from Monday - Thursday<br>from 5:30 PM - 8:30 PM</div>
  <div class="abs dash" style="left:30px;width:256px;top:404px"></div>

  <div class="abs head" style="left:30px;top:420px;width:168px;text-align:right;font-size:24px;line-height:22px">SUBURBS<br><span style="font-size:19px">WE DELIVER TO</span></div>
  <div class="abs icon-fill" style="left:206px;top:410px;width:78px;height:56px;border-radius:20px 20px 28px 28px" role="img" aria-label="Delivery rider on a scooter"></div>
  <div class="abs suburbs" style="left:30px;top:476px">- Beldon<br>- Craigie<br>- Darch<br>- Duncraig<br>- Edgewater</div>
  <div class="abs suburbs" style="left:120px;top:476px">- Greenwood<br>- Hocking<br>- Kingsley<br>- Madeley<br>- Padbury</div>
  <div class="abs suburbs" style="left:212px;top:476px">- Pearsall<br>- Wangara<br>- Woodvale</div>
  <div class="abs charges"><div>DELIVERY CHARGES<b>$5</b></div><div>MINIMUM ORDER VALUE<b>$30</b></div></div>

  <div class="abs head" style="left:38px;top:616px;font-size:19px">BYO (Bring Your Own)</div>
  <div class="abs icon-fill" style="left:42px;top:642px;width:64px;height:92px;border-radius:10px 10px 4px 4px" role="img" aria-label="Wine bottle and glass"></div>
  <div class="abs" style="left:118px;top:648px;font-weight:800;font-size:17px">Wine Only</div>
  <div class="abs" style="left:118px;top:672px;font-size:8px;color:var(--grey)">Corkage per bottle apply</div>
  <svg class="abs" style="left:118px;top:692px" width="38" height="38" viewBox="0 0 38 38" role="img" aria-label="No outside food sign"><circle cx="19" cy="19" r="16" fill="#fff" stroke="#c8262c" stroke-width="3.5"/><line x1="8" y1="8" x2="30" y2="30" stroke="#c8262c" stroke-width="3.5"/></svg>
  <div class="abs head" style="left:162px;top:694px;font-size:12px;line-height:15px">OUTSIDE FOOD<br>IS NOT ALLOWED!</div>

  <section class="abs voucher">
    <h3>DISCOUNT VOUCHERS</h3>
    <p class="bullet">We accept <b>Dining Pass Book Vouchers</b> and <b>Maple Orchard supplied Discount vouchers.</b></p>
    <p class="bullet">Dining Pass Vouchers are eligible only for Dine-In.</p>
  </section>
  <svg class="abs" style="left:524px;top:322px" width="30" height="20" viewBox="0 0 30 20"><circle cx="24" cy="5" r="3.5" fill="none" stroke="#2b2b2b" stroke-width="2"/><circle cx="24" cy="15" r="3.5" fill="none" stroke="#2b2b2b" stroke-width="2"/><path d="M21 7 L2 15 M21 13 L2 5" stroke="#2b2b2b" stroke-width="2"/></svg>
  <div class="abs rule" style="left:302px;width:288px;top:356px"></div>

  <div class="abs head" style="left:315px;top:372px;font-size:16px">BOOKINGS/ORDERS CONTACT</div>
  <svg class="abs" style="left:348px;top:398px" width="22" height="22" viewBox="0 0 24 24"><path fill="#2b2b2b" d="M6.6 10.8a15 15 0 0 0 6.6 6.6l2.2-2.2c.3-.3.7-.4 1-.2 1.1.4 2.3.6 3.6.6.6 0 1 .4 1 1V20c0 .6-.4 1-1 1A17 17 0 0 1 3 4c0-.6.4-1 1-1h3.5c.6 0 1 .4 1 1 0 1.3.2 2.5.6 3.6.1.3 0 .7-.2 1z"/></svg>
  <div class="abs" style="left:382px;top:396px;font-weight:800;font-size:22px">08 5550 0142</div>
  <svg class="abs" style="left:348px;top:430px" width="22" height="15" viewBox="0 0 22 15"><rect width="22" height="15" fill="#2b2b2b"/><path d="M1 1 L11 9 L21 1" stroke="#fff" stroke-width="1.5" fill="none"/></svg>
  <div class="abs" style="left:382px;top:428px;font-weight:700;font-size:12px">admin@mapleorchard.com.au</div>
  <div class="abs pill">www.mapleorchard.com.au</div>
  <svg class="abs" style="left:552px;top:468px" width="20" height="22" viewBox="0 0 20 22"><path d="M2 2 L2 18 L7 13 L11 21 L14 19 L10 12 L17 12 Z" fill="#2b2b2b" stroke="#fff" stroke-width="1"/></svg>
  <div class="abs rule" style="left:302px;width:288px;top:496px"></div>

  <div class="abs head" style="left:315px;top:506px;font-size:19px">PAYMENT METHODS</div>
  <div class="pay" style="left:318px;top:538px;width:46px;background:#3f9a46;color:#fff;font-size:12px">Cash</div>
  <div class="pay" style="left:369px;top:538px;width:48px;background:var(--deep-red);color:#fff">Paylink</div>
  <div class="pay light" style="left:422px;top:538px;width:48px">Vantra</div>
  <div class="pay" style="left:475px;top:538px;width:48px;background:#b13d2b;color:#fff;font-size:9px">Meridian</div>
  <div class="pay" style="left:528px;top:538px;width:48px;background:#9e3d8e;color:#fff">Debit<br>Kredit</div>
  <div class="pay" style="left:318px;top:575px;width:48px;background:#2c86c8;color:#fff;font-size:8px">Northcard</div>
  <div class="pay light" style="left:370px;top:575px;width:46px">Tallis</div>
  <div class="pay light" style="left:421px;top:575px;width:48px">Orbit</div>
  <div class="abs" style="left:476px;top:592px;font-size:8px">*Surcharge of 2.8% apply</div>
  <div class="abs rule" style="left:302px;width:288px;top:616px"></div>

  <div class="abs head" style="left:315px;top:624px;font-size:19px">SERVICES</div>
  <div class="abs icon-fill" style="left:316px;top:662px;width:72px;height:74px;border-radius:24px 24px 0 0" role="img" aria-label="Waiter carrying a serving tray"></div>
  <div class="abs services" style="left:410px;top:652px">
    <p class="bullet">Functions/ Parties</p>
    <p class="bullet">Bulk Cooking</p>
    <p class="bullet">Special Orders</p>
    <p class="bullet">Business Meetings</p>
    <p class="bullet">Seminars/ Presentations</p>
  </div>

  <div class="abs band" style="top:740px"></div>

  <div class="partner" style="left:100px;width:132px;height:42px;border-radius:21px;background:#2a4a9a"></div>
  <div class="partner" style="left:256px;width:96px;height:48px;background:#f4ea1c"></div>
  <div class="partner" style="left:376px;width:48px;height:48px;border-radius:50%;background:#6d6d6d"></div>
  <div class="partner" style="left:448px;width:48px;height:48px;border-radius:50%;background:#3f9a46"></div>
</main>
</body>
</html>
```